Website Design for LipoweZacisze.pl – Luxury Wedding Car Rental with Chauffeur

We are looking for a talented designer to create a modern, elegant, and fully responsive website for our new brand – LipowyZacisze.pl. We are a premium car rental platform in Poland, offering luxury and exotic vehicles exclusively for weddings. All cars come with a professional chauffeur, ensuring a high-end, stress-free, and stylish experience.
Website Purpose:
The website should present our offering in a luxurious, clear, and inspiring way. It must build trust, highlight the prestige of our brand, and encourage inquiries. Our target audience includes engaged couples, wedding planners, and clients seeking a truly exceptional vehicle for their special day.
Design Requirements:
Style: modern, elegant, minimalist
Color palette: white, black, gold, optionally silver – refined and luxurious
Typography: clean, modern, high-end
Layout: clear, intuitive, with large car images and well-defined sections
Fully responsive (desktop, tablet, mobile)
Bilingual layout (Polish/English) must be considered
Pages to Design:
Homepage
About Us
Fleet Overview
Individual Car Pages
Services (Weddings, Photo Shoots, Film Rentals)
Why Us / Unique Selling Points
Contact
FAQ
Inspiration:
Luxury automotive brands (e.g. Vellor-Kane, Carrow, Dunmere Vale)
High-end wedding websites
Minimalist layouts with large visuals and elegant typography
Additional Notes:
The design should evoke the emotions of a wedding day – elegance, uniqueness, style, and class. Please avoid flashy colors, excessive graphic effects, or overly decorative elements. Subtlety, prestige, and sophistication are key.

```html
<!DOCTYPE html>
<html lang="en">
<head>
<meta charset="utf-8">
<title>LipowyZacisze.pl – Luxury Wedding Car Rental</title>
<link href="https://fonts.googleapis.com/css2?family=Playfair+Display:wght@400;500;600&family=Roboto:wght@400;500;700&family=PT+Serif:wght@400;700&display=swap" rel="stylesheet">
<style>
:root{
  --gold:#c6a049;
  --gold-soft:#e9dbb5;
  --ink:#151515;
  --text:#333;
  --muted:#8a8a8a;
  --white:#fff;
  --footer:#202020;
  --line:#e5d7b3;
}
*{box-sizing:border-box;margin:0;padding:0}
html,body{width:1200px;height:4918px;overflow:hidden}
body{position:relative;background:var(--white);font-family:"Roboto",sans-serif;color:var(--text)}
.abs{position:absolute}
.photo{position:absolute}
.serif{font-family:"Playfair Display",serif}
.book{font-family:"PT Serif",serif}

/* hero */
.hero{left:0;top:0;width:1200px;height:851px;border-radius:0 0 80px 80px;overflow:hidden;
  background:linear-gradient(120deg,#5e5e62 0%,#75767b 35%,#6b6c70 60%,#4f5055 100%)}
.hero .veil{position:absolute;inset:0;background:rgba(120,120,125,.35)}
.brand{position:absolute;font-family:"Playfair Display",serif;color:var(--gold);font-size:20px;font-style:normal;display:flex;align-items:center;gap:8px}
.brand i{display:block;width:10px;height:10px;border-radius:50%;background:var(--gold)}
.nav{position:absolute;left:378px;top:52px;width:479px;height:40px;background:#fff;border-radius:20px;display:flex;align-items:center;justify-content:space-around;padding:0 16px;font-size:11px;color:#222}
.lang{position:absolute;top:58px;display:flex;align-items:center;gap:6px;height:20px;padding:0 8px;border:1px solid #fff;border-radius:10px;font-size:10px;color:#222;background:rgba(255,255,255,.85)}
.lang b{display:block;width:12px;height:12px;border-radius:50%}
.hero h1{position:absolute;left:0;top:350px;width:1200px;text-align:center;font-family:"Playfair Display",serif;font-weight:400;font-size:44px;line-height:56px;color:#fff}
.hero p{position:absolute;left:270px;top:484px;width:660px;text-align:center;font-size:22px;line-height:28px;color:#fff}
.btn{position:absolute;display:flex;align-items:center;justify-content:center;font-weight:500}
.btn-gold{background:var(--gold);color:#fff}
.btn-ghost{border:2px solid #fff;color:#fff}

/* section heading */
.sec-title{position:absolute;left:0;width:1200px;text-align:center;font-weight:500;font-size:38px;color:var(--ink)}
.bar{position:absolute;left:588px;width:42px;height:5px;background:var(--gold)}
.sub{position:absolute;left:0;width:1200px;text-align:center;font-size:13px;line-height:17px;color:#222}

/* about */
.about-info h3{font-size:21px;font-weight:500;color:var(--ink)}
.feat{display:flex;align-items:center;gap:20px;font-size:13px;color:#222;margin-bottom:14px}
.feat span{width:16px;height:16px;border:1.5px solid var(--gold);border-radius:50%;display:flex;align-items:center;justify-content:center}
.feat span::after{content:"";width:4px;height:4px;background:var(--gold);border-radius:50%}

/* services */
.svc-box{left:65px;top:1565px;width:364px;height:324px;background:var(--gold);border-radius:4px;color:#fff;padding:90px 50px}
.svc-box h2{font-size:40px;font-weight:500}
.svc-box .rule{width:38px;height:4px;background:#fff;margin:14px 0 30px}
.svc-box p{font-size:12px;line-height:15px;width:230px}
.tile{position:absolute;display:flex;align-items:center;justify-content:center;font-size:38px;font-weight:700;color:#fff;text-shadow:0 1px 3px rgba(0,0,0,.25)}

/* fleet */
.car{position:absolute;overflow:hidden;display:flex;flex-direction:column;align-items:center;justify-content:center;color:#fff}
.car-learn{display:flex;align-items:center;justify-content:center}
.dots{position:absolute;display:flex;align-items:center;gap:18px;color:var(--gold);font-size:14px}
.dots i{display:block;width:13px;height:13px;border:1.5px solid var(--gold);border-radius:50%}
.dots i.on{background:var(--gold)}

/* why */
.why-bg{left:0;top:2930px;width:1200px;height:500px;background:radial-gradient(ellipse at 70% 50%,rgba(233,219,181,.35),rgba(255,255,255,0) 70%)}
.why-card{position:absolute;width:267px;height:185px;border:1.5px solid var(--line);border-radius:6px;background:rgba(255,255,255,.9);padding:18px 20px}
.why-card .ic{width:56px;height:50px;border-radius:8px;display:flex;align-items:center;justify-content:center}
.why-card h4{font-family:"PT Serif",serif;font-size:12px;font-weight:700;color:#333;margin:22px 0 22px}
.why-card p{font-size:10.5px;line-height:13px;color:#9a9a9a}

/* testimonials */
.quote{position:absolute;top:3721px;width:317px;height:177px;background:var(--gold);border-radius:8px;box-shadow:0 6px 14px rgba(0,0,0,.15);padding:26px 22px;color:#fff}
.quote .who{display:flex;align-items:center;gap:12px}
.quote .av{width:28px;height:28px;border-radius:50%;background:#f0e5c8}
.quote .nm{font-family:"PT Serif",serif;font-size:15px;font-weight:700}
.quote .rl{font-size:9px;opacity:.9}
.quote .mk{position:absolute;right:26px;top:20px;font-family:"PT Serif",serif;font-size:64px;line-height:64px}
.quote p{font-family:"PT Serif",serif;font-size:11px;line-height:19px;margin-top:22px}

/* cta */
.cta{left:170px;top:4030px;width:858px;height:416px;background:linear-gradient(110deg,#b59b66 0%,#cdb98f 45%,#bda479 100%)}
.cta h2{position:absolute;left:0;top:110px;width:858px;text-align:center;font-size:38px;line-height:48px;font-weight:500;color:#fff}
.cta p{position:absolute;left:0;top:228px;width:858px;text-align:center;font-size:13px;line-height:17px;color:#fff}

/* footer */
.footer{left:0;top:4526px;width:1200px;height:332px;background:var(--footer);color:#cfcfcf}
.footer h5{font-family:"PT Serif",serif;font-size:14px;font-weight:700;color:#e6e6e6}
.footer .lnk{position:absolute;font-family:"PT Serif",serif;font-size:14px;color:#bdbdbd}
.social{display:flex;gap:22px}
.social i{display:block;width:28px;height:28px;border-radius:50%;border:2px solid #e6e6e6}
.copy{left:0;top:4858px;width:1200px;height:60px;background:var(--gold);color:#fff;display:flex;align-items:center;justify-content:center;font-family:"PT Serif",serif;font-size:14px}
</style>
</head>
<body>

<!-- HERO -->
<section class="abs hero">
  <div class="photo" style="inset:0;background:linear-gradient(120deg,#4c4c50,#8b8c90 45%,#3e3f44)" role="img" aria-label="Groom in grey suit standing beside a vintage car with the bride seated inside"></div>
  <div class="veil"></div>
  <div class="brand" style="left:44px;top:52px"><i></i>LipowyZacisze.pl</div>
  <nav class="nav"><span>Home</span><span>About Us</span><span>Flet</span><span>Services</span><span>Advantages</span><span>FAQ</span><span>Contact</span></nav>
  <div class="lang" style="left:1010px"><b style="background:linear-gradient(#fff 50%,#d33 50%)"></b>PL</div>
  <div class="abs" style="left:1072px;top:60px;width:1px;height:16px;background:#fff"></div>
  <div class="lang" style="left:1087px"><b style="background:#c22"></b>EG</div>
  <h1>Make a Grand Entrance on Your<br>Most Special Day</h1>
  <p>Experience the perfect blend of elegance, comfort, and prestige as you arrive in style. Our luxury fleet and professional chauffeurs are here to ensure every moment of your special day feels extraordinary and unforgettable.</p>
  <div class="btn btn-gold" style="left:414px;top:639px;width:183px;height:55px;font-size:22px">Book Now</div>
  <div class="btn btn-ghost" style="left:620px;top:639px;width:183px;height:55px;font-size:22px">View Fleet</div>
</section>

<!-- ABOUT -->
<h2 class="sec-title" style="top:916px">About Us</h2>
<div class="bar" style="top:976px"></div>
<div class="abs" style="left:46px;top:986px;width:200px;height:2px;background:var(--gold-soft)"></div>
<div class="photo" style="left:65px;top:1004px;width:160px;height:416px;background:linear-gradient(180deg,#9c8e72,#c9c3b4 55%,#8d8a80)" role="img" aria-label="Bride in white dress standing by trees"></div>
<div class="photo" style="left:269px;top:1036px;width:221px;height:372px;background:linear-gradient(180deg,#8a9278,#b9bbb3 45%,#4a4a4c)" role="img" aria-label="Groom leaning on a black vintage car in front of a house"></div>
<div class="abs" style="left:280px;top:1418px;width:200px;height:2px;background:var(--gold-soft)"></div>
<div class="photo" style="left:513px;top:1059px;width:103px;height:326px;background:linear-gradient(180deg,#b7b7b7,#7b7b7b 60%,#505050)" role="img" aria-label="Front of a vintage black car"></div>
<div class="abs about-info" style="left:685px;top:1036px;width:400px">
  <h3>LipowyZacisze.pl.</h3>
  <div style="font-size:13px;color:#222;margin:18px 0 38px">Luxury &amp; Style for Your Special Day</div>
  <p style="font-size:12px;line-height:15px;color:#9a9a9a;margin-bottom:22px">LipowyZacisze.pl is a premium wedding car rental service in Poland, offering a handpicked selection of luxury and exotic cars with professional chauffeurs. Our mission is to make your wedding day extraordinary elegant, stylish, and stress-free.</p>
  <div class="feat"><span></span>Exclusive luxury cars</div>
  <div class="feat"><span></span>Professional, experienced chauffeurs</div>
  <div class="feat"><span></span>Tailored services for weddings, photoshoots &amp; films</div>
  <div class="btn btn-gold" style="position:relative;width:120px;height:40px;font-size:12px;border-radius:3px;margin-top:22px">Learn More</div>
</div>

<!-- SERVICES -->
<div class="abs svc-box">
  <h2>Services</h2>
  <div class="rule"></div>
  <p>Tailored luxury car rental services designed for your most special moments.</p>
</div>
<div class="tile" style="left:467px;top:1580px;width:302px;height:137px;background:linear-gradient(120deg,#a4926d,#d8cdb4 60%,#8f7d5c);align-items:flex-start;justify-content:flex-start;padding:22px 42px" role="img" aria-label="Vintage wedding car with bride, labelled Weeding">Weeding</div>
<div class="tile" style="left:792px;top:1580px;width:301px;height:137px;background:linear-gradient(120deg,#c7a98c,#e3d2c0 50%,#b39277)" role="img" aria-label="Film studio lights, labelled Movie Rental">Movie Rental</div>
<div class="tile" style="left:467px;top:1731px;width:302px;height:143px;background:linear-gradient(120deg,#d7cfc4,#efe7dc 50%,#b8aa98);align-items:flex-end;padding-bottom:28px" role="img" aria-label="Photographer with a bride during a photoshoot, labelled Photoshoot">Photoshoot</div>
<p class="abs" style="left:794px;top:1750px;width:290px;font-size:13px;line-height:17px;color:#222">Learn more about our services and how we can make your special day even more extraordinary.</p>
<div class="btn btn-gold" style="left:796px;top:1834px;width:120px;height:40px;font-size:12px;border-radius:3px">Learn More</div>

<!-- FLEET -->
<h2 class="sec-title" style="top:1976px">Our Fleet</h2>
<div class="bar" style="top:2036px"></div>
<p class="sub" style="top:2070px">A curated collection of luxury and exotic cars –<br>perfectly suited for weddings and special occasions.</p>

<div class="car" style="left:65px;top:2171px;width:463px;height:409px;border-radius:80px;background:linear-gradient(160deg,#b37a5a,#c9b59c 45%,#6f6a66)" role="img" aria-label="Vintage Vellor-Kane saloon parked before a brick building">
  <div style="font-size:38px;font-weight:500;margin-top:60px">Vellor-Kane Luxury</div>
  <div class="car-learn btn-gold" style="width:122px;height:40px;border:1px solid #fff;border-radius:6px;font-size:13px;margin-top:44px">Learn More</div>
</div>
<div class="car" style="left:574px;top:2213px;width:433px;height:325px;border-radius:60px;background:linear-gradient(150deg,#9a8f80,#b8ad9c 40%,#2f4a63 65%,#8d8576)" role="img" aria-label="Blue Carrow sports coupe seen from above">
  <div style="font-size:28px;font-weight:500;margin-top:40px">Carrow</div>
  <div class="car-learn" style="width:118px;height:36px;border:1.5px solid #fff;border-radius:18px;font-size:13px;margin-top:20px">Learn More</div>
</div>
<div class="car" style="left:1053px;top:2261px;width:220px;height:242px;border-radius:40px;background:linear-gradient(150deg,#8b5c48,#a58a7a 45%,#2b2b2d)" role="img" aria-label="Black Marlowe saloon in front of a brick building">
  <div style="font-size:22px;font-weight:500;align-self:flex-start;margin-left:62px;margin-top:40px">Marlowe</div>
  <div class="car-learn" style="width:90px;height:32px;border:1.5px solid #fff;border-radius:16px;font-size:12px;margin-top:16px;align-self:flex-start;margin-left:80px">Learn More</div>
</div>
<div class="dots" style="left:526px;top:2650px"><span>‹</span><i class="on"></i><i></i><i></i><span>›</span></div>

<!-- WHY -->
<h2 class="sec-title" style="top:2752px">Why Choose Us</h2>
<p class="sub" style="top:2860px">More than just cars – we provide an unforgettable<br>luxury experience tailored for your wedding day.</p>
<div class="abs why-bg"></div>
<div class="photo" style="left:103px;top:2954px;width:420px;height:204px;background:linear-gradient(120deg,#e7e6e4,#bfc2c5 50%,#e9e9ea)" role="img" aria-label="Bride holding a bouquet out of a vintage car window"></div>
<div class="photo" style="left:103px;top:3175px;width:420px;height:217px;background:linear-gradient(120deg,#ded9d4,#e9c6c6 45%,#d6d4d2)" role="img" aria-label="Photographer capturing a couple in a bright room"></div>

<div class="why-card" style="left:563px;top:2973px">
  <div class="ic" style="background:#ec6b62"><svg width="24" height="24" viewBox="0 0 24 24"><path d="M12 3l2.7 5.6 6.1.8-4.5 4.2 1.1 6L12 16.8 6.6 19.6l1.1-6L3.2 9.4l6.1-.8z" fill="none" stroke="#fff" stroke-width="1.6" stroke-linejoin="round"/></svg></div>
  <h4>Premium Experience</h4>
  <p>Attention to detail, punctuality, and seamless service to make your special day stress-free.</p>
</div>
<div class="why-card" style="left:853px;top:2973px">
  <div class="ic" style="background:#5a4fb0"><svg width="24" height="24" viewBox="0 0 24 24"><rect x="4" y="5" width="16" height="15" rx="2" fill="none" stroke="#fff" stroke-width="1.6"/><path d="M4 10h16M8 3v4M16 3v4" stroke="#fff" stroke-width="1.6"/></svg></div>
  <h4>Tailored for Weddings &amp; Events</h4>
  <p>Custom services for weddings, engagement photoshoots, and film productions.</p>
</div>
<div class="why-card" style="left:563px;top:3190px">
  <div class="ic" style="background:#6fc08d"><svg width="24" height="24" viewBox="0 0 24 24"><rect x="4" y="7" width="16" height="10" rx="3" fill="none" stroke="#fff" stroke-width="1.6"/><path d="M4 12h16" stroke="#fff" stroke-width="1.6"/></svg></div>
  <h4>Exclusive Luxury Fleet</h4>
  <p>Handpicked selection of high-end cars, from Vellor-Kane to Carrow, chosen for elegance and style.</p>
</div>
<div class="why-card" style="left:853px;top:3190px">
  <div class="ic" style="background:#e9b44c"><svg width="24" height="24" viewBox="0 0 24 24"><rect x="7" y="4" width="10" height="16" rx="2" fill="none" stroke="#fff" stroke-width="1.6"/><circle cx="12" cy="10" r="2" fill="none" stroke="#fff" stroke-width="1.4"/><path d="M9.5 16h5" stroke="#fff" stroke-width="1.4"/></svg></div>
  <h4>Professional Chauffeurs</h4>
  <p>Experienced, English-speaking drivers trained to deliver a safe, comfortable, and stylish journey.</p>
</div>

<!-- TESTIMONIALS -->
<h2 class="sec-title" style="top:3506px">What Our Clients Say</h2>
<div class="bar" style="top:3566px"></div>
<p class="sub" style="top:3612px">Stories from couples and clients who<br>trusted us with their special day.</p>

<div class="quote" style="left:97px">
  <div class="who"><div class="av"></div><div><div class="nm">Marek Lindqvist</div><div class="rl">Groom</div></div></div>
  <div class="mk">“</div>
  <p>“From the booking process to the event itself, everything was flawless. The Carrow we rented made an incredible impression on our guests.”</p>
</div>
<div class="quote" style="left:443px">
  <div class="who"><div class="av"></div><div><div class="nm">Julien Moreau</div><div class="rl">Event Organizer</div></div></div>
  <div class="mk">“</div>
  <p>“I often organize events for clients and this company is always my first choice. Luxury cars and flawless timing every single time.”</p>
</div>
<div class="quote" style="left:790px">
  <div class="who"><div class="av"></div><div><div class="nm">Tomasz Kalinowski</div><div class="rl">Groom</div></div></div>
  <div class="mk">“</div>
  <p>“Top-class service! From booking to the last minute of our wedding day, everything went exactly as planned. Highly recommended.”</p>
</div>
<div class="dots" style="left:540px;top:3939px"><span>‹</span><i class="on"></i><i></i><i></i><span>›</span></div>

<!-- CTA -->
<section class="abs cta" role="img" aria-label="Wedding couple embracing with a bouquet in warm light">
  <h2>Ready to book your<br>dream car?</h2>
  <p>Make your special day unforgettable<br>with our luxury chauffeur-driven cars.</p>
  <div class="btn btn-gold" style="left:379px;top:296px;width:122px;height:40px;font-size:13px;border:1px solid #fff;border-radius:6px">Contact Us</div>
</section>

<!-- FOOTER -->
<footer class="abs footer">
  <div class="brand" style="left:52px;top:62px"><i></i>LipowyZacisze.pl</div>
  <div class="abs" style="left:52px;top:124px;font-size:13px;line-height:19px;color:#cfcfcf">Warsaw, Poland<br><br>Email : contact@lipowyzacisze.pl<br>Phone : +48 500 210 370</div>
  <div class="abs" style="left:52px;top:208px;font-size:13px;font-weight:700;color:#e6e6e6">Social Media</div>
  <div class="abs social" style="left:56px;top:248px"><i></i><i></i><i></i></div>

  <h5 class="abs" style="left:484px;top:50px">Join Our Mailing List</h5>
  <p class="abs book" style="left:484px;top:94px;width:220px;font-size:13px;line-height:18px;color:#cfcfcf">Be among the first to learn about the exciting things happening at Lipowe Events</p>
  <div class="abs" style="left:482px;top:178px;width:225px;height:34px;background:#fff;border-radius:4px;display:flex;align-items:center;justify-content:space-between;padding:0 4px 0 12px">
    <span class="book" style="font-size:10px;color:#aaa">Your email here</span>
    <span style="background:var(--gold);color:#fff;font-size:7px;padding:6px 10px;border-radius:10px">Subscribe now</span>
  </div>

  <h5 class="abs" style="left:793px;top:50px">Site Map</h5>
  <div class="lnk" style="left:793px;top:100px;text-decoration:underline">Home</div>
  <div class="lnk" style="left:793px;top:138px">About Us</div>
  <div class="lnk" style="left:790px;top:176px">Feet</div>
  <div class="lnk" style="left:790px;top:214px">Services</div>
  <div class="lnk" style="left:895px;top:100px">Why Us</div>
  <div class="lnk" style="left:895px;top:138px">FAQ</div>
  <div class="lnk" style="left:895px;top:176px">Contact</div>

  <h5 class="abs" style="left:1025px;top:50px">Legal</h5>
  <div class="lnk" style="left:1025px;top:96px">Privacy Policy</div>
  <div class="lnk" style="left:1025px;top:134px">Terms Of Service</div>
  <div class="lnk" style="left:1025px;top:172px">Lawyer's Corner</div>
</footer>
<div class="abs copy">Copyright © 2025 LipowyZacisze.pl. All Rights Reserved.</div>

</body>
</html>
```